Our swimming pool service needs your help with letterhead

Letterhead for small swimming pool service- We would like a professional look with a creative layout- must be compatible with LedgerNest forms (sample attached)
No more than 2 colors in graphics

Target Market(s)

Homeowners/ Contractors

Font styles to use
Sans Serif

Colors
33a6d7
85cae6

Requirements
Must have
• Logo (file attached)
• Compatible with LedgerNest (sample attached)
• Mailing address- P.O. Box 58, Cedar Hollow NY 11592
• phone- (631) 529-6180
• email- marcdoylewater@mailbrook.net
• Licensed & Insured
Nice to have
• Small slogan- Examples:Family owned and operated for 25 years, 25 years of trusted service
• Creative layout
Should not have
• Blue color must be same as blue in our logo
• No thick lines of color
• No design in middle of page

```html
<!DOCTYPE html>
<html lang="en">
<head>
<meta charset="utf-8">
<title>Marc T. Doyle Pool Service – Invoice Letterhead</title>
<link href="https://fonts.googleapis.com/css2?family=Montserrat:ital,wght@0,400;0,500;0,600;1,400&family=Roboto+Mono:wght@400&display=swap" rel="stylesheet">
<style>
  :root{
    --navy:#22375a;
    --sky:#5fa8dc;
    --mist:#d3d3d3;
    --ink:#4a4a4a;
    --rule:#9a9a9a;
    --backdrop:#ececec;
    --paper:#ffffff;
  }
  *{margin:0;padding:0;box-sizing:border-box}
  html,body{width:998px;height:1200px;overflow:hidden;background:var(--backdrop)}
  body{position:relative;font-family:"Montserrat",sans-serif;color:var(--ink)}
  .sheet{position:absolute;left:75px;top:0;width:847px;height:1200px;background:var(--paper);overflow:hidden}

  .brand{position:absolute;left:51px;top:92px;display:flex;align-items:center;gap:12px;color:var(--navy);font-weight:600}
  .brand-dot{width:34px;height:34px;border-radius:50%;background:var(--sky);flex:none}
  .brand-name{line-height:1.05}
  .brand-name .top{display:block;font-size:19px;letter-spacing:3px}
  .brand-name .main{display:block;font-size:31px;letter-spacing:1px}

  .contact{position:absolute;left:572px;top:90px;height:68px;border-left:1.5px solid var(--navy);padding-left:14px;font-size:13.5px;line-height:19.5px;color:var(--ink)}
  .contact li{list-style:none;display:flex;align-items:center;gap:6px}
  .contact svg{width:10px;height:10px;flex:none}

  .box{position:absolute;border:1px solid var(--rule)}
  .cell-head{font-size:12.5px;font-weight:500;text-align:center;color:#333}

  .bill-to{left:79px;top:243px;width:349px;height:149px}
  .bill-to .cell-head{height:34px;line-height:34px;border-bottom:1px solid var(--rule)}
  .bill-to address{font-style:italic;text-align:center;font-size:17px;line-height:22px;padding-top:14px;color:#444}

  .meta .cell-head{height:33px;line-height:33px;border-bottom:1px solid var(--rule)}
  .meta .value{height:34px;line-height:34px;text-align:center;font-size:15px;color:#333}
  .date{left:51px;top:454px;width:142px;height:69px}
  .invoice-no{left:483px;top:454px;width:174px;height:69px}
  .terms{left:656px;top:454px;width:140px;height:69px}

  .items{left:51px;top:522px;width:745px;height:482px}
  .items .cols{position:absolute;inset:0;display:grid;grid-template-columns:432px 73px 100px 1fr}
  .items .col{border-right:1px solid var(--rule)}
  .items .col:last-child{border-right:none}
  .items .head-row{position:absolute;left:0;right:0;top:0;height:34px;border-bottom:1px solid var(--rule);display:grid;grid-template-columns:432px 73px 100px 1fr}
  .items .head-row span{font-size:12.5px;font-weight:500;text-align:center;line-height:30px;color:#333}
  .line-items{position:absolute;left:0;right:0;top:38px;font-family:"Roboto Mono",monospace;font-size:13px;line-height:20px;color:#333}
  .line-items .row{display:grid;grid-template-columns:432px 73px 100px 1fr}
  .line-items .desc{padding-left:3px;letter-spacing:1.5px}
  .line-items .num{text-align:right;padding-right:6px}

  .payable{position:absolute;left:90px;width:312px;top:1013px;text-align:center;font-style:italic;font-size:13.5px;line-height:21px;color:#444}
  .total{left:556px;top:1003px;width:240px;height:49px;display:flex;align-items:center;justify-content:space-between;padding:0 40px 0 14px;border-top:none}
  .total .label{font-style:italic;font-size:22px;color:#444}
  .total .sum{font-size:21px;color:#333}

  .footer-band{position:absolute;left:0;bottom:0;width:847px;height:80px;background:linear-gradient(180deg,var(--mist) 0%,var(--sky) 40%,var(--navy) 100%)}
</style>
</head>
<body>
<main class="sheet">
  <header>
    <div class="brand">
      <span class="brand-dot"></span>
      <span class="brand-name"><span class="top">MARC T. DOYLE</span><span class="main">POOL SERVICE</span></span>
    </div>
    <ul class="contact">
      <li>P.O. Box 58, Cedar Hollow NY 11592</li>
      <li><svg viewBox="0 0 10 10"><path d="M2 1l2 2-1 1.3a6 6 0 0 0 2.7 2.7L7 6l2 2-1.3 1.3C4.5 9 1 5.5.7 2.3z" fill="var(--sky)"/></svg>(631) 529-6180</li>
      <li><svg viewBox="0 0 10 10"><rect x=".5" y="2" width="9" height="6.5" fill="none" stroke="var(--sky)"/><path d="M.5 2L5 5.5 9.5 2" fill="none" stroke="var(--sky)"/></svg>marcdoylewater@mailbrook.net</li>
      <li><svg viewBox="0 0 10 10"><rect x=".5" y="2" width="9" height="6.5" fill="none" stroke="var(--sky)"/><path d="M.5 2L5 5.5 9.5 2" fill="none" stroke="var(--sky)"/></svg>Licensed &amp; Insured</li>
    </ul>
  </header>

  <section class="box bill-to">
    <div class="cell-head">BILL TO:</div>
    <address>SAMPLE<br>123 AVENUE<br>ANYWHERE, USA</address>
  </section>

  <div class="box meta date"><div class="cell-head">DATE</div><div class="value">9/11/2019</div></div>
  <div class="box meta invoice-no"><div class="cell-head">INVOICE NO.</div><div class="value">11676</div></div>
  <div class="box meta terms"><div class="cell-head">TERMS</div><div class="value">Due on receipt</div></div>

  <section class="box items">
    <div class="cols"><div class="col"></div><div class="col"></div><div class="col"></div><div class="col"></div></div>
    <div class="head-row"><span>DESCRIPTION</span><span>QTY</span><span>RATE</span><span>AMOUNT</span></div>
    <div class="line-items">
      <div class="row"><span class="desc">LABOR</span><span></span><span class="num">0.00</span><span class="num">0.00T</span></div>
      <div class="row"><span class="desc">Sales Tax</span><span></span><span class="num">8.625%</span><span class="num">0.00</span></div>
    </div>
  </section>

  <p class="payable">CHECK PAYABLE TO MARC T. DOYLE.<br>CHARGE BY PHONE.</p>
  <div class="box total"><span class="label">Total:</span><span class="sum">$0.00</span></div>

  <div class="footer-band" role="img" aria-label="Decorative water-themed footer band in grey, sky blue and navy"></div>
</main>
</body>
</html>
```